Price Calculator as Responsive Web App to support Sales People

We need to build a simple micro web app to support sales people in making quotes. We already have a backend that can take a number of parameters and create a quote. We need put a responsive web app on top of this so that our people on the road can easily do their price simulations.

We need two pages. One for the input and another for the results. No menus, navigations, etc. It is 6 different inputs as shown with boxes in the sketch. They don't need to be boxed, but some of them have a bit of instruction text that clearly need to belong to the input.

This needs to be responsive, but first and foremost designed for smartphones. I have included a background gradient that we would like to use -- or a variant of it. We expect this to be delivered as HTML/CSS + images so that we can quickly write a few pieces of JavaScript ourselves to wire it up to our price simulator.

Industry/Entity Type

Information Technology

Coding

Coded - Design and coding required

Number of Pages Required

2 page

Font styles to use
Sans Serif

Requirements
Must have
• Responsive design
• Easy to wire up JavaScript to the HTML/CSS
Nice to have
• Some quick way to pick number of months. +/- buttons to add remove a year or 3 months. Same thing with number of items. Add 10 or 5 quickly.
• Maybe some parallax effect while scrolling as long as it is not distracting.
Should not have
• Toolbars, Menus, Navigations, Banners, etc. This is just a single micro app.

```html
<!DOCTYPE html>
<html lang="en">
<head>
<meta charset="utf-8">
<title>Price Calculator</title>
<link href="https://fonts.googleapis.com/css2?family=Saira+Semi+Condensed:wght@500;600&family=Open+Sans:wght@400;600&display=swap" rel="stylesheet">
<style>
:root{
  --page:#e6e6e6;
  --white:#ffffff;
  --band:#f0f0f0;
  --ink:#222222;
  --body:#444444;
  --icon:#8c8c8c;
  --red:#e31515;
  --darkred:#8e0000;
  --blue:#2f8fe8;
  --sky:#3cc4f0;
  --total:#0b64a0;
  --cap:#990000;
  --radio:#9a9a9a;
}
*{box-sizing:border-box;margin:0;padding:0}
html,body{width:1200px;height:834px;overflow:hidden}
body{background:var(--page);position:relative;font-family:"Open Sans",sans-serif;color:var(--ink)}
.heading{font-family:"Saira Semi Condensed",sans-serif;font-weight:600;font-size:14px;line-height:18px;color:var(--ink)}
.badge{position:absolute;left:37px;width:38px;height:38px;border-radius:50%;background:var(--icon);border:2px solid #bdbdbd;display:flex;align-items:center;justify-content:center}
.badge svg{width:22px;height:22px;fill:none;stroke:#fff;stroke-width:1.6;stroke-linecap:round;stroke-linejoin:round}

/* input panel */
.inputs{position:absolute;left:10px;top:10px;width:554px;height:812px}
.field{position:relative;padding:20px 30px 0 92px}
.field:nth-child(odd){background:var(--white)}
.field:nth-child(even){background:var(--band)}
.stepper{height:64px;padding:0;display:flex;align-items:center}
.stepper .badge{top:12px}
.stepper .heading{position:absolute;left:92px;top:22px}
.controls{position:absolute;left:166px;top:22px;display:flex;align-items:center;height:20px}
.btn{width:19px;height:19px;border-radius:50%;color:#fff;font-size:8px;font-weight:600;display:flex;align-items:center;justify-content:center;margin-right:4px}
.btn.minus{background:var(--red)}
.btn.minus-big{background:var(--darkred)}
.btn.plus{background:var(--blue)}
.btn.plus-big{background:var(--sky)}
.amount{width:56px;height:20px;border:1px solid #cfcfcf;border-radius:3px;background:#fff;font-size:11px;font-weight:600;text-align:center;line-height:18px;margin:0 6px 0 8px}
.unit{font-size:10.5px;font-weight:600;margin-right:12px}
.choice .badge{top:12px}
.options{list-style:none;margin-top:3px;display:grid;grid-auto-flow:column}
.choice.engine .options{grid-template-rows:repeat(2,22px);grid-template-columns:203px auto}
.choice.storage .options{grid-template-rows:repeat(3,22px);grid-template-columns:112px auto}
.choice.tip .options{grid-template-rows:repeat(3,22px)}
.choice.elastic .options{grid-template-rows:repeat(2,22px)}
.option{display:flex;align-items:center;font-size:10px;font-weight:600;color:var(--ink)}
.radio{width:15px;height:15px;border-radius:50%;border:1.5px solid #9c9c9c;background:#fff;margin-right:9px;flex:none}
.radio.checked{background:var(--radio);box-shadow:inset 0 0 0 2px #fff}
.note{font-size:10px;line-height:14px;color:var(--body);margin-top:8px}
.engine{height:160px}
.storage{height:182px}
.tip{height:182px}
.elastic{height:160px}

/* results panel */
.results{position:absolute;left:636px;top:10px;width:554px;height:812px;background:var(--white)}
.summary{width:100%;border-collapse:collapse}
.summary th{font-family:"Saira Semi Condensed",sans-serif;font-weight:500;font-size:13px;height:68px;padding-top:16px;color:var(--ink)}
.summary td{height:49px;font-size:10px;font-weight:600;text-align:center}
.summary tbody tr:nth-child(odd){background:var(--band)}
.summary .label{text-align:left;position:relative;padding-left:106px}
.summary .label .heading{font-size:13px}
.summary .badge{left:62px;top:7px;width:34px;height:34px}
.summary .badge svg{width:19px;height:19px}
.summary tr.total{background:var(--total)!important;color:#fff}
.summary tr.cap{background:var(--cap)!important;color:#fff}
.summary tr.total .heading,.summary tr.cap .heading{color:#fff}
.col-label{width:200px}
.col-month{width:160px}
.chart{position:absolute;left:96px;top:420px;width:362px;height:208px;background:linear-gradient(180deg,#d9d9d9 0%,#b0b0b0 35%,#e01010 60%,#9a0000 100%)}
.caption{position:absolute;left:64px;top:661px;width:440px;font-size:10px;line-height:14px;color:var(--body)}
</style>
</head>
<body>

<form class="inputs">
  <section class="field stepper">
    <span class="badge"><svg viewBox="0 0 24 24"><circle cx="12" cy="12" r="8"/><path d="M12 7v5l3 2"/></svg></span>
    <span class="heading">Duration</span>
    <div class="controls">
      <span class="btn minus">-1</span><span class="btn minus-big">-12</span>
      <span class="amount">24</span><span class="unit">months</span>
      <span class="btn plus">+1</span><span class="btn plus-big">+12</span>
    </div>
  </section>
  <section class="field stepper">
    <span class="badge"><svg viewBox="0 0 24 24"><path d="M4 19v-4h3v4zM9 19v-6h3v6zM14 19v-9h3v9zM19 19V6"/></svg></span>
    <span class="heading">Count</span>
    <div class="controls">
      <span class="btn minus">-1</span><span class="btn minus-big">-10</span>
      <span class="amount">100</span><span class="unit">items</span>
      <span class="btn plus">+1</span><span class="btn plus-big">+10</span>
    </div>
  </section>
  <section class="field choice engine">
    <span class="badge"><svg viewBox="0 0 24 24"><path d="M5 9h10l3 3h2v4h-2l-2 2H7l-2-2H3v-5h2z"/><circle cx="10" cy="13" r="1.5"/><circle cx="14" cy="13" r="1.5"/></svg></span>
    <h2 class="heading">Engine Power (beyond standard)</h2>
    <ul class="options">
      <li class="option"><span class="radio"></span>$360/year - Bronze power</li>
      <li class="option"><span class="radio checked"></span>$600/year - Silver power</li>
      <li class="option"><span class="radio"></span>$1M/year - Gold power</li>
      <li class="option"><span class="radio"></span>$3M/year - Platinum super</li>
    </ul>
    <p class="note">Lorem ipsum dolor sit amet, consectetuer adipiscing elit, sed diam nonummy nibh euismod cidunt ut laoreet dolore magna aliquam erat volutpat. Ut wisi enim ad minim veniam, quis trud exerci tation ullamcorper suscipit lobortis nisl ut aliquip ex ea commodo consequat.</p>
  </section>
  <section class="field choice storage">
    <span class="badge"><svg viewBox="0 0 24 24"><path d="M12 4v10M8 10l4 4 4-4M5 13v6h14v-6"/></svg></span>
    <h2 class="heading">Shared Storage Addition</h2>
    <ul class="options">
      <li class="option"><span class="radio"></span>10 Kg</li>
      <li class="option"><span class="radio checked"></span>50 Kg</li>
      <li class="option"><span class="radio"></span>100 Kg</li>
      <li class="option"><span class="radio"></span>500 Kg</li>
      <li class="option"><span class="radio"></span>1 T</li>
    </ul>
    <p class="note">Lorem ipsum dolor sit amet, consectetuer adipiscing elit, sed diam nonummy nibh euismod cidunt ut laoreet dolore magna aliquam erat volutpat. Ut wisi enim ad minim veniam, quis trud exerci tation ullamcorper suscipit lobortis nisl ut aliquip ex ea commodo consequat.</p>
  </section>
  <section class="field choice tip">
    <span class="badge"><svg viewBox="0 0 24 24"><circle cx="12" cy="12" r="7"/><path d="M12 8v8M8 12h8"/></svg></span>
    <h2 class="heading">Additional Tip</h2>
    <ul class="options">
      <li class="option"><span class="radio"></span>15%</li>
      <li class="option"><span class="radio checked"></span>18%</li>
      <li class="option"><span class="radio"></span>20%</li>
    </ul>
    <p class="note">Lorem ipsum dolor sit amet, consectetuer adipiscing elit, sed diam nonummy nibh euismod cidunt ut laoreet dolore magna aliquam erat volutpat. Ut wisi enim ad minim veniam, quis trud exerci tation ullamcorper suscipit lobortis nisl ut aliquip ex ea commodo consequat.</p>
  </section>
  <section class="field choice elastic">
    <span class="badge"><svg viewBox="0 0 24 24"><path d="M5 5l5 5M5 5v4M5 5h4M19 19l-5-5M19 19v-4M19 19h-4"/></svg></span>
    <h2 class="heading">Elastic Extension</h2>
    <ul class="options">
      <li class="option"><span class="radio"></span>30%</li>
      <li class="option"><span class="radio checked"></span>50%</li>
    </ul>
    <p class="note">Lorem ipsum dolor sit amet, consectetuer adipiscing elit, sed diam nonummy nibh euismod cidunt ut laoreet dolore magna aliquam erat volutpat. Ut wisi enim ad minim veniam, quis trud exerci tation ullamcorper suscipit lobortis nisl ut aliquip ex ea commodo consequat.</p>
  </section>
</form>

<main class="results">
  <table class="summary">
    <thead>
      <tr><th class="col-label"></th><th class="col-month">Per Month</th><th>Per Year</th></tr>
    </thead>
    <tbody>
      <tr><td class="label"><span class="badge"><svg viewBox="0 0 24 24"><path d="M4 19v-4h3v4zM9 19v-6h3v6zM14 19v-9h3v9zM19 19V6"/></svg></span><span class="heading">Items</span></td><td>350</td><td>4200</td></tr>
      <tr><td class="label"><span class="badge"><svg viewBox="0 0 24 24"><path d="M5 9h10l3 3h2v4h-2l-2 2H7l-2-2H3v-5h2z"/><circle cx="10" cy="13" r="1.5"/><circle cx="14" cy="13" r="1.5"/></svg></span><span class="heading">Engine</span></td><td>250</td><td>3000</td></tr>
      <tr><td class="label"><span class="badge"><svg viewBox="0 0 24 24"><path d="M12 4v10M8 10l4 4 4-4M5 13v6h14v-6"/></svg></span><span class="heading">Storage</span></td><td>200</td><td>2400</td></tr>
      <tr><td class="label"><span class="badge"><svg viewBox="0 0 24 24"><circle cx="12" cy="12" r="7"/><path d="M12 8v8M8 12h8"/></svg></span><span class="heading">Tip</span></td><td>52</td><td>630</td></tr>
      <tr class="total"><td class="label"><span class="heading">Total</span></td><td>852</td><td>10230</td></tr>
      <tr class="cap"><td class="label"><span class="heading">Cap</span></td><td>1278</td><td>15345</td></tr>
    </tbody>
  </table>

  <div class="chart" role="img" aria-label="Illustrated cost trend graphic in red and grey"></div>

  <p class="caption">Lorem ipsum dolor sit amet, consectetuer adipiscing elit, sed diam nonummy nibh euismod cidunt ut laoreet dolore magna aliquam erat volutpat. Ut wisi enim ad minim veniam, quis trud exerci tation ullamcorper suscipit lobortis nisl ut aliquip ex ea commodo consequat.</p>
</main>

</body>
</html>
```